Property management company looking for modern card design

We at Blue Heron Partners provides property management services for its residential and commercial properties, with expertise in all categories of multifamily, industrial and office projects throughout California.

We need a business card design that is professional and modern designed business card. In our field, clients get hundreds of business cards, we would like our card to stand out.

Please avoid small print.

Target Market(s)

Professionals and high end clients

Industry/Entity Type

Financial Planning

Contact Information for Business Card

Company Name: Blue Heron Partners, Name, email, license #, phone number, website blueheronpartners.com

Font styles to use
Sans Serif

Requirements
Must have
• The card design needs to be adaptable because there is a possibly we will be expanding into different sectors other than real estate. The card design should be focused on financial planning and asset management.
Nice to have
• Modern and simple business card. Eye catching. Non-standard size/shaped cards would be great.
• blueheronpartners.com
Should not have
• Too many bright color or any pictures or shapes of real estate stuff.

```html
<!DOCTYPE html>
<html lang="en">
<head>
<meta charset="utf-8">
<title>Blue Heron Partners — Business Cards</title>
<link rel="stylesheet" href="https://fonts.googleapis.com/css2?family=Cabin:wght@400;600;700&display=swap">
<style>
  :root {
    --backdrop: #dcdac8;
    --kraft: #c9a46c;
    --kraft-dark: #bd9760;
    --mark-red: #ec1c2e;
    --brand-red: #b0141d;
    --ink: #2a2b30;
    --ink-soft: #474852;
    --rule: #3c3d44;
  }
  * { box-sizing: border-box; margin: 0; padding: 0; }
  html, body {
    width: 900px;
    height: 1200px;
    overflow: hidden;
    background: var(--backdrop);
    font-family: "Cabin", sans-serif;
  }
  .canvas {
    position: relative;
    width: 900px;
    height: 1200px;
  }
  .card {
    position: absolute;
    background: radial-gradient(ellipse at 40% 35%, var(--kraft) 0%, var(--kraft-dark) 100%);
    box-shadow: 0 2px 6px rgba(0,0,0,0.18);
    overflow: hidden;
  }
  .card--front {
    left: 314px; top: 141px;
    width: 302px; height: 527px;
  }
  .card--back {
    left: 187px; top: 723px;
    width: 527px; height: 301px;
  }
  .brand-dot {
    position: absolute;
    left: 50%;
    width: 64px; height: 64px;
    margin-left: -32px;
    border-radius: 50%;
    background: var(--mark-red);
  }
  .card--front .brand-dot { top: 82px; }
  .card--back .brand-dot { top: 94px; }
  .brand-name {
    position: absolute;
    left: 0; right: 0;
    text-align: center;
    font-weight: 600;
    font-size: 25px;
    letter-spacing: 4px;
    color: var(--brand-red);
    line-height: 1;
  }
  .card--front .brand-name { top: 179px; }
  .card--back .brand-name { top: 185px; }
  .rule {
    position: absolute;
    left: 43px; right: 0;
    height: 3px;
    background: var(--rule);
  }
  .rule--top { top: 251px; }
  .rule--mid { top: 324px; }
  .rule--low { top: 408px; }
  .holder {
    position: absolute;
    right: 33px; top: 262px;
    text-align: right;
    color: var(--ink);
  }
  .holder__name {
    font-size: 30px;
    font-weight: 600;
    line-height: 1.1;
  }
  .holder__title {
    font-size: 12.5px;
    margin-top: 3px;
  }
  .contact {
    position: absolute;
    right: 33px; top: 418px;
    text-align: right;
    color: var(--ink);
    font-size: 12px;
    font-weight: 700;
    line-height: 22px;
  }
  .contact__web {
    font-size: 17px;
    color: var(--ink-soft);
    margin-top: 4px;
    line-height: 1;
  }
  .back-web {
    position: absolute;
    left: 0; right: 0;
    top: 263px;
    text-align: center;
    font-size: 18px;
    font-weight: 700;
    color: var(--ink-soft);
  }
</style>
</head>
<body>
<main class="canvas">
  <section class="card card--front" aria-label="Business card front">
    <div class="brand-dot"></div>
    <div class="brand-name">Blue Heron</div>
    <div class="rule rule--top"></div>
    <div class="holder">
      <div class="holder__name">Daniel Hale</div>
      <div class="holder__title">managing director</div>
    </div>
    <div class="rule rule--mid"></div>
    <div class="rule rule--low"></div>
    <div class="contact">
      <div>daniel.hale@blueheronpartners.com</div>
      <div>555-010-0142</div>
      <div>License Nr:000001</div>
      <div class="contact__web">blueheronpartners.com</div>
    </div>
  </section>

  <section class="card card--back" aria-label="Business card back">
    <div class="brand-dot"></div>
    <div class="brand-name">Blue Heron</div>
    <div class="back-web">blueheronpartners.com</div>
  </section>
</main>
</body>
</html>
```